TOASTED COCONUT CHIPS

My company is a food company specialised in coconut products. The subject project is to design the package bag and respective simple shipping case for toasted coconut chips for two flavors: one is original and the other is cinnamon. I also need a logo design for the brand "pimlo".

I would like the bag looks simple, classy and attractive. Or the other way that it could look cute and fun.

The design will include two flavors: original/sea salt and cinnamon
The design need to be fit in 40g pouch bag and 20g bag.
Need the design of the bag and subsequently the shipping case.

Target Market(s)

age 8 to 40
sell in cafeteria and vending machine

Industry/Entity Type

It Company

Logo Text

simple and direct

Requirements
Must have
• golden coconut chips picture on the front side.
• the bag should looks clean but attractive.
• Otherwise, it has to be very colourful to attract eye balls.
• I need the design can be fit in a 40g pouch and 20g cutie size bag
Should not have
• Should not look Asian food.

```html
<!DOCTYPE html>
<html lang="en">
<head>
<meta charset="utf-8">
<title>Pimlo Toasted Coconut Chips – Original 20 g</title>
<link href="https://fonts.googleapis.com/css2?family=Oswald:wght@500&family=Dancing+Script:wght@600&family=Fira+Sans+Condensed:wght@200;400;500&display=swap" rel="stylesheet">
<style>
  :root {
    --bg: #e6e6e6;
    --bag: #f4f4f4;
    --seal: #ececec;
    --seal-line: #d9d9d9;
    --gold: #c8922b;
    --gold-deep: #b27a1a;
    --gold-light: #e2a93a;
    --pattern: #ead3a2;
    --ink: #2f2f2f;
    --white: #ffffff;
  }
  * { box-sizing: border-box; margin: 0; padding: 0; }
  html, body { width: 1200px; height: 1070px; overflow: hidden; }
  body { background: var(--bg); position: relative; }

  .pouch {
    position: absolute; left: 338px; top: 160px;
    width: 532px; height: 772px;
    background: var(--bag);
  }
  .seal {
    position: absolute; left: 0; width: 100%;
    background: repeating-linear-gradient(180deg, var(--seal) 0 3px, var(--seal-line) 3px 4px);
  }
  .seal--top { top: 0; height: 36px; }
  .seal--bottom { bottom: 0; height: 58px; }

  .wave-pattern {
    position: absolute; left: 51px; top: 0; width: 421px; height: 400px;
    background: linear-gradient(180deg, var(--pattern), #f0dfba);
    opacity: 0.85;
  }
  .brand-band {
    position: absolute; left: 196px; top: 0; width: 132px; height: 324px;
    background: linear-gradient(160deg, var(--gold-deep) 0%, var(--gold-light) 45%, var(--gold) 100%);
  }
  .brand-name {
    position: absolute; left: 196px; top: 262px; width: 132px;
    text-align: center; color: var(--white);
    font-family: "Fira Sans Condensed", sans-serif; font-weight: 500;
    font-size: 44px; line-height: 1;
  }

  .headline {
    position: absolute; left: 51px; top: 410px; width: 424px;
    font-family: "Oswald", sans-serif; font-weight: 500;
    color: var(--gold); font-size: 33px; line-height: 36px;
    letter-spacing: -0.3px; white-space: nowrap;
  }
  .description {
    position: absolute; left: 51px; top: 494px; width: 290px;
    font-family: "Dancing Script", cursive; font-weight: 600;
    color: var(--gold); font-size: 17.5px; line-height: 24px;
  }
  .flavour-rule {
    position: absolute; left: 336px; top: 496px; width: 2px; height: 136px;
    background: var(--gold);
  }
  .flavour {
    position: absolute; left: 346px; top: 494px;
    font-family: "Fira Sans Condensed", sans-serif; font-weight: 200;
    color: var(--gold); font-size: 60px; line-height: 64px;
  }
  .divider {
    position: absolute; left: 51px; top: 644px; width: 421px; height: 2px;
    background: var(--gold);
  }
  .claims {
    position: absolute; left: 51px; top: 656px;
    display: grid; grid-template-columns: 69px 92px auto;
    font-family: "Fira Sans Condensed", sans-serif; font-weight: 400;
    color: var(--ink); font-size: 11px; line-height: 16px;
    list-style: none; text-transform: uppercase; white-space: nowrap;
  }
  .net-weight {
    position: absolute; right: 60px; top: 668px;
    font-family: "Fira Sans Condensed", sans-serif; font-weight: 500;
    color: var(--ink); font-size: 27px; line-height: 1;
  }
</style>
</head>
<body>
  <main class="pouch">
    <div class="seal seal--top"></div>

    <div class="wave-pattern" role="img" aria-label="Decorative gold wave pattern of toasted coconut curls"></div>
    <div class="brand-band" role="img" aria-label="Golden toasted coconut chips photo"></div>
    <p class="brand-name">pimlo</p>

    <h1 class="headline">THIN CURVE COCONUT MEAT<br>TOASTED TO LIGHT GOLDEN COLOR</h1>

    <p class="description">Pimlo Toasted Coconut Chips are made from premium coconuts and slowly toasted to perfection. It is absolutely a tasty and healthy snack on their own or as an accompaniment with salads, ice cream or yogurt.</p>

    <div class="flavour-rule"></div>
    <p class="flavour">ORIGI-<br>NAL</p>

    <div class="divider"></div>

    <ul class="claims">
      <li>Not fired</li><li>Dairy free</li><li>No artifical color</li>
      <li>Vegan</li><li>No cholesterol</li><li>No artificial flavouring</li>
      <li>Gluten free</li><li>No preservative</li><li>Good source of fiber</li>
    </ul>
    <p class="net-weight">20 g (0.7 oz)</p>

    <div class="seal seal--bottom"></div>
  </main>
</body>
</html>
```